Business card with logo for a family psychologist

I need a business card for my private practice in the urban Chicago area as a psychologist. I see families and individuals who are going through difficult times - divorce, separation, illness, or trauma. I want to project hopefulness, competence, and caring.

Target Market(s)

Adults, other professionals - such as physicans and lawyers

Industry/Entity Type

Health Care

Contact Information for Business Card

Front should have my name and credentials; back should have location information including my email, phone

Font styles to use
Serif
Decorative
Script

Requirements
Must have
• Unique logo
Should not have
• No pictures or icons of people; no black

```html
<!DOCTYPE html>
<html lang="en">
<head>
<meta charset="utf-8">
<title>Dana Marlowe, Ph.D. — Business Card</title>
<link href="https://fonts.googleapis.com/css2?family=Fjalla+One&family=Lato:wght@400;700&display=swap" rel="stylesheet">
<style>
  :root {
    --page-bg: #e8e5e1;
    --card-white: #ffffff;
    --ink-blue: #1f4e8c;
    --ink-grey: #555a60;
    --mark-faint: #ececec;
    --back-top: #4588c6;
    --back-mid: #285a92;
    --back-bottom: #1b4273;
    --mark-green: #6cc155;
    --on-dark: #ffffff;
  }
  html, body {
    margin: 0;
    padding: 0;
    width: 1200px;
    height: 1000px;
    overflow: hidden;
    background: var(--page-bg);
  }
  .canvas {
    position: relative;
    width: 1200px;
    height: 1000px;
  }
  .card {
    position: absolute;
    left: 284px;
    width: 626px;
    height: 357px;
    border-radius: 28px;
    overflow: hidden;
  }
  /* Front side */
  .card-front {
    top: 140px;
    background: var(--card-white);
    box-shadow: 0 3px 10px rgba(0,0,0,0.12);
  }
  .front-details {
    position: absolute;
    left: 62px;
    top: 106px;
    font-family: "Lato", sans-serif;
    color: var(--ink-grey);
    font-size: 15px;
    line-height: 18px;
  }
  .holder-name {
    margin: 0;
    font-weight: 700;
    font-size: 19px;
    line-height: 24px;
    color: var(--ink-blue);
  }
  .holder-title { margin: 0; }
  .address { margin: 16px 0 0; }
  .contact-list {
    list-style: none;
    margin: 12px 0 0;
    padding: 0;
  }
  .contact-list li {
    display: flex;
    align-items: center;
    gap: 7px;
  }
  .contact-icon { width: 13px; height: 13px; fill: var(--ink-blue); }
  .front-mark {
    position: absolute;
    left: 392px;
    top: 75px;
    width: 200px;
    height: 200px;
    border-radius: 50%;
    background: var(--mark-faint);
  }
  /* Back side */
  .card-back {
    top: 531px;
    background: linear-gradient(to bottom, var(--back-top) 0%, var(--back-mid) 32%, var(--back-bottom) 55%, var(--back-bottom) 100%);
  }
  .back-identity {
    position: absolute;
    left: 112px;
    top: 140px;
    display: flex;
    align-items: center;
    gap: 20px;
  }
  .back-mark {
    width: 76px;
    height: 76px;
    border-radius: 50%;
    background: var(--mark-green);
  }
  .back-name {
    margin: 0;
    font-family: "Fjalla One", sans-serif;
    font-size: 40px;
    line-height: 44px;
    color: var(--on-dark);
    letter-spacing: 0.5px;
  }
  .back-title {
    margin: 2px 0 0;
    font-family: "Lato", sans-serif;
    font-size: 20px;
    color: var(--on-dark);
    letter-spacing: 0.3px;
  }
</style>
</head>
<body>
<main class="canvas">
  <section class="card card-front">
    <div class="front-details">
      <p class="holder-name">Dana Marlowe, Ph.D.</p>
      <p class="holder-title">Licensed Clinical Psychologist</p>
      <p class="address">240 W. Lakeview Ave Suite 310<br>Chicago, Illinois 60614</p>
      <ul class="contact-list">
        <li>
          <svg class="contact-icon" viewBox="0 0 16 16" aria-hidden="true"><path d="M1 5c0-2 2-3 7-3s7 1 7 3v1h-4V5H5v1H1zM4 7h8l2 6H2z"/></svg>
          <span>312-555-0148</span>
        </li>
        <li>
          <svg class="contact-icon" viewBox="0 0 16 16" aria-hidden="true"><path d="M1 3h14v10H1z M1 3l7 6 7-6" stroke="#fff" stroke-width="1"/></svg>
          <span>drdanamarlowe@example.com</span>
        </li>
      </ul>
    </div>
    <div class="front-mark" aria-hidden="true"></div>
  </section>

  <section class="card card-back">
    <div class="back-identity">
      <div class="back-mark" aria-hidden="true"></div>
      <div>
        <p class="back-name">Dana Marlowe, Ph.D.</p>
        <p class="back-title">Licensed Clinical Psychologist</p>
      </div>
    </div>
  </section>
</main>
</body>
</html>
```